Redesigned Website for Investment Firm/Investment Education Company

DO NOT CONTACT PRIVATELY - ALL PRIVATE MESSAGES WILL BE IGNORED

Please avoid complex design techniques. Should be professional and modern with a linear design approach.

Please see uploaded file for existing content

The company is The Birchwood Equity Trust, LLC, and they provide investment education and services. Their Guided Capital Stewardship academic program offers a two-year analyst program for undergraduate students, combining academic, research, money management, and career components. The company manages $5.5 million in assets and follows the value investing philosophy of Gerald P. Ashcombe. The website should have a modern and professional design, with a linear layout that is not too busy.

The website should consist of five pages:

1 Welcome page: This page should have a top image with a ClipNest video play button or embedded ClipNest video that highlights the company's services and offerings.

Underneath that there should be an overview section of the services offered, with a textual description underneath that highlights the company's services and offerings.

Below the overview section, there should be an "Our Investment Approach" section with a clear and concise description of the company's investment philosophy. This section should describe the company's focus on value investing, and its approach to identifying investment opportunities through intensive research of individual companies.

The page should have a modern and professional design, with a clear overview of the company and its services. It should include some key features that set it apart from its competitors, and a call to action for users to learn more or sign up for their programs.

2 Programs page: This page should emphasize that the classes have a fall, spring, and summer schedule. The page should include a table showing the available classes in each season. The design should be modern and professional, with a focus on making it easy for users to understand the different programs and their benefits.

3 Directors page: This page should provide users with information and bios of the directors of the business. The design should be clean and modern, with each director's photo and a detailed bio.

4 Senior Analysts page: This page should provide users with information and bios of the senior analysts of the business. The design should be clean and modern, with each analyst's photo and a detailed bio.

5 Junior Analysts page: This page should provide users with information and bios of the junior analysts of the business. The design should be clean and modern, with each analyst's photo and a detailed bio.

DO NOT INCLUDE
- search bar
- login buttons

Target Market(s)

Students looking to get into investing

Industry/Entity Type

Finance/Investing

Number of Pages Required

5+ page

Colors
F0912C
F2A743
F7CA91
FBE8D2
FDF5EE

Requirements
Should not have
• - search bar - login buttons

```html
<!DOCTYPE html>
<html lang="en">
<head>
<meta charset="utf-8">
<title>The Birchwood Equity Trust, LLC — Pages</title>
<link href="https://fonts.googleapis.com/css2?family=Open+Sans:wght@400;600;700&display=swap" rel="stylesheet">
<style>
:root{
  --orange:#F0912C;
  --orange-2:#F2A743;
  --peach:#F7CA91;
  --cream:#FBE8D2;
  --ivory:#FDF5EE;
  --ink:#333;
  --dark:#2b2b2b;
  --grey-bg:#f2f2f2;
}
*{box-sizing:border-box;margin:0;padding:0}
html,body{width:790px;height:1200px;overflow:hidden;background:#fff;font-family:'Open Sans',sans-serif;color:var(--ink)}
.board{position:absolute;left:0;top:0;width:1568px;height:2382px;transform:scale(.5038);transform-origin:0 0}
.page{position:absolute;top:40px;width:445px;background:#fff;box-shadow:0 2px 10px rgba(0,0,0,.18);overflow:hidden}
.hero{position:relative;height:111px;background:linear-gradient(135deg,#5e5e5e,#a9a9a9 45%,#7a7a7a 80%,#c4c4c4)}
.brand{position:absolute;left:41px;top:8px;color:#fff;font-size:8px;font-weight:600}
.nav{position:absolute;right:41px;top:10px;display:flex;gap:10px;font-size:5px;color:#fff}
.nav .on{position:relative}
.nav .on::after{content:"";position:absolute;left:50%;top:8px;width:2px;height:2px;background:#fff;border-radius:50%}
.hero-title{position:absolute;left:0;right:0;bottom:17px;text-align:center;color:#fff;font-size:18px;font-weight:700}
.block{position:relative;overflow:hidden}
.block.orange{background:var(--orange);color:#fff}
.block.grey{background:var(--grey-bg)}
.photo{position:absolute;width:119px;height:138px;background:linear-gradient(160deg,#d9d4cf,#8d8782);z-index:2}
.deco{position:absolute;background:var(--cream);z-index:1}
.block.orange .deco{background:var(--peach);opacity:.85}
.frame{position:absolute;border:1.5px solid var(--orange);z-index:3}
.block.orange .frame{border-color:#fff}
.bio{position:absolute;z-index:2}
.bio h3{font-size:8.5px;font-weight:700;color:var(--orange);line-height:12px;margin-bottom:6px}
.block.orange .bio h3{color:#fff}
.bio p{font-size:5.2px;line-height:10.4px;text-align:justify;margin-bottom:5px}
.bio .mail{color:var(--orange)}
.block.orange .bio .mail{color:#fff;text-decoration:underline}
.section-title{font-size:15px;font-weight:700;color:var(--orange);text-align:center}
.lead{font-size:5.2px;line-height:10.4px}
.table-card{position:absolute;left:41px;width:363px;background:#f4f4f4;padding:9px}
.sched{width:100%;border-collapse:collapse;background:#fff;font-size:5px;box-shadow:0 1px 3px rgba(0,0,0,.12)}
.sched th{background:var(--orange);color:#fff;text-align:left;font-weight:400;padding:4px 12px;height:15px}
.sched td{padding:6px 12px;line-height:10.5px;vertical-align:top;border-bottom:1px solid #e4e4e4}
.sched th:first-child{border-radius:3px 0 0 0}
.sched th:last-child{border-radius:0 3px 0 0}
.footer{position:relative;height:129px;background:var(--dark);color:#fff;padding:14px 41px 0}
.footer .f-brand{position:absolute;left:41px;top:24px;font-size:8px;font-weight:600}
.footer .f-col{position:absolute;top:16px;font-size:5px;line-height:10.5px}
.footer .f-col b{font-weight:600;display:flex;align-items:center;gap:4px}
.footer .legal{position:absolute;left:41px;right:41px;top:56px;font-size:3.6px;line-height:9.8px;color:#ddd}
.ext{position:absolute;left:41px;right:41px;text-align:center}
</style>
</head>
<body>
<div class="board">

<!-- Programs page -->
<section class="page" style="left:43px;height:742px">
  <header class="hero" role="img" aria-label="Greyscale photo of a hand reviewing financial charts">
    <div class="brand">The Birchwood Equity Trust, LLC</div>
    <nav class="nav"><span>Welcome</span><span class="on">Programs</span><span>Directors</span><span>Senior Analysts</span><span>Junior Analysts</span></nav>
    <h1 class="hero-title">Program Details</h1>
  </header>
  <div class="block" style="height:501px">
    <div class="deco" style="left:0;top:66px;width:58px;height:96px"></div>
    <div class="frame" style="left:-2px;top:112px;width:12px;height:70px;border-left:none"></div>
    <div class="deco" style="left:424px;top:445px;width:21px;height:92px;z-index:0"></div>
    <div class="frame" style="left:385px;top:490px;width:62px;height:26px;z-index:0"></div>
    <h2 style="position:absolute;left:41px;top:30px;font-size:15px;font-weight:700;color:var(--orange)">Junior Analysts</h2>
    <p class="lead" style="position:absolute;left:185px;top:31px;width:219px">Junior Analysts are recruited to work in The Birchwood Equity Trust, LLC while they participate in the Guided Capital Stewardship program and they complete the courses outlined in the schedule below.</p>
    <div class="table-card" style="top:75px">
      <table class="sched">
        <tr><th>Fall</th><th>Spring</th><th>Summer</th></tr>
        <tr><td>FIN 466 Value Investing<br>FIN 463 - Financial<br>Modeling for Investment Banking I</td><td>FIN 473 Control Investing<br>FIN 459 Intro to Derivatives</td><td>FIN 469 - Distress Investing<br>Maymester</td></tr>
        <tr><td>BET Weekly seminar</td><td>BET Weekly seminar</td><td>Hallbrook House or Dunmore Center, NYC</td></tr>
        <tr><td>Quantro Certification</td><td>Wall Street Road Show</td><td>Internship with a Financial Services Firm</td></tr>
        <tr><td>Wall Street Road Show</td><td></td><td></td></tr>
      </table>
    </div>
    <h2 style="position:absolute;left:41px;top:249px;font-size:15px;font-weight:700;color:var(--orange)">Senior Analysts</h2>
    <p class="lead" style="position:absolute;left:185px;top:250px;width:219px;text-align:justify">Senior Analysts are the second-year analysts in The Birchwood Equity Trust, LLC. To continue to be retained as analysts in the Fund, students must be able to contribute investable ideas on their own. Failure to do so constitutes cause for automatic removal from the Fund analyst roster, even though the students may continue to participate in the Guided Capital Stewardship academic program at their option.</p>
    <div class="table-card" style="top:328px;background:#fff;padding:0 0">
      <table class="sched">
        <tr><th>Fall</th><th>Spring</th><th>Summer</th></tr>
        <tr><td>FIN 466 Value Investing<br>FIN 463 - Financial<br>Modeling for Investment Banking I</td><td>FIN 473 Control Investing<br>FIN 459 Intro to Derivatives</td><td>FIN 469 - Distress Investing<br>Maymester</td></tr>
        <tr><td>BET Weekly seminar</td><td>BET Weekly seminar</td><td>Hallbrook House or Dunmore Center, NYC</td></tr>
        <tr><td>Quantro Certification</td><td>Wall Street Road Show</td><td>Internship with a Financial Services Firm</td></tr>
        <tr><td>Wall Street Road Show</td><td></td><td></td></tr>
      </table>
    </div>
  </div>
  <footer class="footer">
    <div class="f-brand">The Birchwood Equity Trust, LLC</div>
    <div class="f-col" style="left:185px"><b><svg width="5" height="6" viewBox="0 0 10 12"><path d="M5 0a4 4 0 0 1 4 4c0 3-4 8-4 8S1 7 1 4a4 4 0 0 1 4-4z" fill="#fff"/></svg>VISIT US</b>Managing Director<br>The GPA Ashcombe Professor of Finance</div>
    <div class="f-col" style="left:302px"><b><svg width="6" height="6" viewBox="0 0 12 12"><path d="M2 1l2 0 1 3-1.5 1a7 7 0 0 0 3.5 3.5L8 7l3 1v2a1 1 0 0 1-1 1A9 9 0 0 1 1 2a1 1 0 0 1 1-1z" fill="#fff"/></svg>CONTACT US</b>555.014.2290<br>r.ostrano@birchwoodequity.com</div>
    <div class="legal">The Birchwood Equity Trust, LLC is a private investments fund organized as a Delaware Limited Liability Company. The Fund is an entity operated by a board of directors. Managing Directors, and recruited students of the Gerald P. Ashcombe School of Management.<br>This website serves information and educational purposes only.<br>The website does not constitute an offer to sell or a solicitation of an offer to buy securities. Such offers may be made only pursuant to a private placement memorandum, and securities will be sold only to investors who meet certain suitability requirements.<br>2023 The Birchwood Equity Trust, LLC. All Rights Reserved.</div>
  </footer>
</section>

<!-- Directors page -->
<section class="page" style="left:552px;height:1717px">
  <header class="hero" role="img" aria-label="Greyscale photo of city office towers">
    <div class="brand">The Birchwood Equity Trust, LLC</div>
    <nav class="nav"><span>Welcome</span><span>Programs</span><span class="on">Directors</span><span>Senior Analysts</span><span>Junior Analysts</span></nav>
    <h1 class="hero-title">Fund Directors</h1>
  </header>

  <div class="block" style="height:240px">
    <div class="deco" style="left:25px;top:22px;width:110px;height:100px"></div>
    <div class="frame" style="left:17px;top:105px;width:40px;height:26px"></div>
    <div class="photo" role="img" aria-label="Portrait photo of director Harold T. Wexmoor" style="left:41px;top:38px"></div>
    <div class="bio" style="left:186px;top:34px;width:217px">
      <h3>Harold T. Wexmoor '83 BS,</h3>
      <p>Mr. Wexmoor is the founder of a value investment institute and chief executive of an investment management firm he founded in 1989. He has been a portfolio manager and analyst for more than 20 years. He started his investment career at a large insurance company, where he managed utility and equity income funds. Before forming his own firm, he was a partner in a private investment management firm specializing in long and short utility strategies.</p>
      <p>Mr. Wexmoor is a 1983 summa cum laude graduate of the university, where he now serves as a member of the Board of Trustees, sitting on the Investment and Endowment Committee. In addition to giving significant support to his alma mater, he was moved by a desire to bring the markets alive to the students, which led to his generous gift that helped the Gerald P. Ashcombe School of Management create a center with the ambitious, straightforward mission of offering an unparalleled investment education to its students.</p>
    </div>
  </div>

  <div class="block orange" style="height:251px">
    <div class="deco" style="left:262px;top:90px;width:120px;height:103px"></div>
    <div class="frame" style="left:356px;top:140px;width:65px;height:28px"></div>
    <div class="photo" role="img" aria-label="Portrait photo of Professor Rafael Ostrano" style="left:283px;top:22px"></div>
    <div class="bio" style="left:41px;top:20px;width:218px">
      <h3>Professor Rafael Ostrano,</h3>
      <p>Dr. Ostrano is the Gerald P. Ashcombe Professor of Finance and the Managing Director of the Fund. After earning his PhD in 1989, he joined the university faculty to offer courses on value, control and distress investing as well as in derivative securities. He is also the faculty advisor to the Guided Capital Stewardship program. He is the co-author of <u>Troubled Assets: Methods and Practice</u> and <u>Foundations of Equity Appraisal</u> with Gerald P. Ashcombe.</p>
      <p>His research specialties are in the areas of value, control and distress investing as well as derivative securities. His work has been presented at academic and industry forums on managed futures and derivatives. He has been a visiting professor at a business school and a visiting scholar at a commodity trading commission. He has consulted with utilities and power companies on issues related to trading electricity, as well as with global companies like a Spanish futures exchange, and served as a consultant to leading securities firms under a global settlement.</p>
    </div>
  </div>

  <div class="block" style="height:219px">
    <div class="deco" style="left:25px;top:75px;width:18px;height:110px"></div>
    <div class="frame" style="left:80px;top:150px;width:93px;height:26px"></div>
    <div class="photo" role="img" aria-label="Portrait photo of director Marian L. Callow" style="left:41px;top:30px"></div>
    <div class="bio" style="left:186px;top:26px;width:217px">
      <h3>Marian L. Callow '77, '79 MBA,</h3>
      <p>Mrs. Callow is a managing partner at an advisory merchant bank that she co-founded in 2005. She heads up the Boston office and is the senior banker focusing on the asset management industry. Prior to becoming an investment banker, she was a leading adviser to the financial services industry for 25 years, specializing in strategic marketing, planning, product design and the implementation of innovative service strategies. She holds a bachelor's degree and an MBA from the school.</p>
      <p>Mrs. Callow serves on the board of directors of a women's leadership circle, an advisory board on financial services, and a real estate fund board. She is a member of the University Board of Trustees and was previously on the Alumni Association Board of Directors. She is a member of the Women in Business Club, a frequent lecturer at the school and assists with the Birchwood Equity Trust.</p>
    </div>
  </div>

  <div class="block orange" style="height:198px">
    <div class="deco" style="left:345px;top:0;width:100px;height:105px"></div>
    <div class="frame" style="left:404px;top:85px;width:20px;height:22px"></div>
    <div class="photo" role="img" aria-label="Portrait photo of director Edwin Farrow" style="left:283px;top:22px"></div>
    <div class="bio" style="left:41px;top:20px;width:218px">
      <h3>Edwin Farrow '59</h3>
      <p>Mr. Farrow is chairman of his own enterprises, a position he has held since 1997. His career on Wall Street has included serving as managing director of equity markets at a major broker, president and CEO of a trading firm, and CEO of an investment house. In 2003 he was selected to go on as independent research consultant to the investment clients of a global bank, under an agreement with the state attorney general and the securities commission.</p>
      <p>Mr. Farrow serves on several boards and committees, including a private bank and trust, an energy company and a realty firm. Since graduating from the school in 1959, he has played an active role at the university. He received the school's Alumnus of the Year Award in 1993. He is a life trustee and former vice-chair of the University Board of Trustees and a member of the investment committee.</p>
    </div>
  </div>

  <div class="block" style="height:196px">
    <div class="deco" style="left:25px;top:75px;width:18px;height:95px"></div>
    <div class="frame" style="left:80px;top:148px;width:93px;height:26px"></div>
    <div class="photo" role="img" aria-label="Portrait photo of Professor Anton Seliga" style="left:41px;top:28px"></div>
    <div class="bio" style="left:186px;top:72px;width:217px">
      <h3>Professor Anton Seliga,</h3>
      <p>Dr. Seliga is the Chair of the Finance Department at the Gerald P. Ashcombe School of Management. He is a Professor of Finance and holds a chair in international business as well as the director of the center for international business.</p>
    </div>
  </div>

  <div class="block grey" style="height:236px">
    <div class="deco" style="left:335px;top:138px;width:110px;height:98px"></div>
    <div class="frame" style="left:356px;top:106px;width:65px;height:26px"></div>
    <h2 class="section-title" style="position:absolute;left:0;right:0;top:26px">Internal Auditor</h2>
    <div class="photo" role="img" aria-label="Portrait photo of Professor Helen Marsk" style="left:283px;top:70px"></div>
    <div class="bio" style="left:41px;top:66px;width:218px">
      <h3 style="color:var(--ink)">Professor Helen Marsk, CPA</h3>
      <p>Dr. Marsk is a Professor of Accounting Practice at the Gerald P. Ashcombe School of Management. She earned a bachelor's degree in accounting and worked in a regional office of a large firm as an auditor in financial services, manufacturing, and not-for-profit markets. After earning her MBA, she joined a corporate leadership program. After extensive travelling with the program, she returned to the area to work in manufacturing operations. She taught accounting, business statistics and finance courses at a state college from 2000 to 2007 and served as a Department Chair for four years. Her primary teaching responsibilities include Managerial Accounting and Advanced Financial Accounting in the undergraduate program, and Principles of Fraud Examination in the graduate program.</p>
    </div>
  </div>

  <div class="block" style="height:136px">
    <div class="deco" style="left:0;top:78px;width:18px;height:58px"></div>
    <div class="frame" style="left:-2px;top:122px;width:34px;height:14px;border-left:none;border-bottom:none"></div>
    <h2 class="section-title" style="position:absolute;left:0;right:0;top:22px">External Auditor</h2>
    <div class="ext" style="top:56px;font-size:7.2px;font-weight:700;line-height:15px">Ridley &amp; Thorne Certified Public Accountants, PLLC.<br>(previously known as Pell &amp; Darrow)</div>
    <div class="ext lead" style="top:95px;left:55px;right:55px">The Birchwood Equity Trust, LLC. is a private investment fund organized as a Delaware Limited Liability Company. The Fund is an entity wholly operated by students of the Gerald P. Ashcombe School of Management.</div>
  </div>

  <footer class="footer">
    <div class="f-brand">The Birchwood Equity Trust, LLC</div>
    <div class="f-col" style="left:185px"><b><svg width="5" height="6" viewBox="0 0 10 12"><path d="M5 0a4 4 0 0 1 4 4c0 3-4 8-4 8S1 7 1 4a4 4 0 0 1 4-4z" fill="#fff"/></svg>VISIT US</b>Managing Director<br>The GPA Ashcombe Professor of Finance</div>
    <div class="f-col" style="left:302px"><b><svg width="6" height="6" viewBox="0 0 12 12"><path d="M2 1l2 0 1 3-1.5 1a7 7 0 0 0 3.5 3.5L8 7l3 1v2a1 1 0 0 1-1 1A9 9 0 0 1 1 2a1 1 0 0 1 1-1z" fill="#fff"/></svg>CONTACT US</b>555.014.2290<br>r.ostrano@birchwoodequity.com</div>
    <div class="legal">The Birchwood Equity Trust, LLC is a private investments fund organized as a Delaware Limited Liability Company. The Fund is an entity operated by a board of directors. Managing Directors, and recruited students of the Gerald P. Ashcombe School of Management.<br>This website serves information and educational purposes only.<br>The website does not constitute an offer to sell or a solicitation of an offer to buy securities. Such offers may be made only pursuant to a private placement memorandum, and securities will be sold only to investors who meet certain suitability requirements.<br>2023 The Birchwood Equity Trust, LLC. All Rights Reserved.</div>
  </footer>
</section>

<!-- Senior Analysts page -->
<section class="page" style="left:1061px;height:2295px">
  <header class="hero" role="img" aria-label="Greyscale photo of business people silhouetted against office windows">
    <div class="brand">The Birchwood Equity Trust, LLC</div>
    <nav class="nav"><span>Welcome</span><span>Programs</span><span>Directors</span><span class="on">Senior Analysts</span><span>Junior Analysts</span></nav>
    <h1 class="hero-title">Senior Analysts</h1>
  </header>

  <div class="block" style="height:240px">
    <div class="deco" style="left:25px;top:22px;width:110px;height:100px"></div>
    <div class="frame" style="left:17px;top:105px;width:40px;height:26px"></div>
    <div class="photo" role="img" aria-label="Portrait photo of analyst Clara Wendt" style="left:41px;top:38px"></div>
    <div class="bio" style="left:186px;top:34px;width:217px">
      <h3>Clara Wendt, '22 BS Finance &amp; Information Management</h3>
      <p>Clara is a junior pursuing a degree in Finance at the Gerald P. Ashcombe School of Management and minoring in Information Management and Technology. Her passion for finance stems from growing up with a mother in finance and a father who was constantly teaching her about the market and investing, which then led her to invest in her own personal portfolio. On top of being involved in the Birchwood Equity Trust, she is involved in the honors program, a sorority and a financial literacy initiative that teaches local middle school students the fundamentals of finance. This past summer she was a finance intern at a media company. She believes the Trust will help her gain the skills and knowledge necessary for a successful career in sales and trading.</p>
      <p>You can contact Clara at: <span class="mail">clara.wendt@birchwoodequity.com</span></p>
    </div>
  </div>

  <div class="block orange" style="height:191px">
    <div class="deco" style="left:262px;top:60px;width:120px;height:103px"></div>
    <div class="frame" style="left:350px;top:120px;width:70px;height:28px"></div>
    <div class="photo" role="img" aria-label="Portrait photo of analyst Nora Castell" style="left:283px;top:22px"></div>
    <div class="bio" style="left:41px;top:20px;width:218px">
      <h3>Nora Castell, '22 BS Finance and Management</h3>
      <p>Nora is a junior in the Gerald P. Ashcombe School of Management. She is double majoring in finance and management. Her passion for finance began when working at her family's accounting firm. Outside of the classroom she is involved in a group which tutors students from disadvantaged socioeconomic backgrounds in investing and provides them with resources to invest. She also works at a fitness studio. She hopes to gain a deeper understanding of finance through the Trust and translate this to a career in the financial services industry. This summer she will be interning in business consulting.</p>
      <p>You can contact Nora at: <span class="mail">nora.castell@birchwoodequity.com</span></p>
    </div>
  </div>

  <div class="block" style="height:197px">
    <div class="deco" style="left:80px;top:120px;width:95px;height:65px"></div>
    <div class="frame" style="left:17px;top:80px;width:40px;height:26px"></div>
    <div class="photo" role="img" aria-label="Portrait photo of analyst Owen Pryce" style="left:41px;top:35px"></div>
    <div class="bio" style="left:186px;top:32px;width:217px">
      <h3>Owen Pryce, '22 BS Finance and Business Management,</h3>
      <p>Owen is a junior in the Gerald P. Ashcombe School of Management and is currently double majoring in finance and business management while minoring in economics. His curiosity for finance began at a young age while watching stock tickers dart across the screen on the news before school. Throughout his time at the university, he has found different ways to pursue this passion, through being a member of the investment club, managing his own portfolio, and being a student tutor. Besides finance he has a passion for fitness, skiing, and basketball. He hopes to hone his skills to pursue a career within asset management.</p>
      <p>You can contact Owen at: <span class="mail">owen.pryce@birchwoodequity.com</span></p>
    </div>
  </div>

  <div class="block orange" style="height:232px">
    <div class="deco" style="left:272px;top:120px;width:110px;height:92px"></div>
    <div class="frame" style="left:350px;top:140px;width:70px;height:28px"></div>
    <div class="photo" role="img" aria-label="Portrait photo of analyst Luke Varanda" style="left:283px;top:22px"></div>
    <div class="bio" style="left:41px;top:28px;width:218px">
      <h3>Luke Varanda, '22 BS Finance and Accounting,</h3>
      <p>Luke is a junior in the Gerald P. Ashcombe School of Management, with a double major in finance and accounting. From a young age, he developed a great interest in business, more specifically, securities and investing. He was first introduced to the stock market in high school and from that moment on, he wanted to learn as much as he could about the fascinating craft that is investing. He is now a junior analyst at the Trust where he is ecstatic of the opportunities to learn and gain real-world experience within finance. Through his time so far he has been involved with many organizations and volunteer groups, deeming it important to give back to the community. He hopes to utilize the knowledge and experience gained and apply it to his career. This summer he is a tax consultant intern where he will help clients analyze the tax effect of complex decisions, reduce overall tax rates, and pursue performance objectives.</p>
      <p>You can contact Luke at: <span class="mail">luke.varanda@birchwoodequity.com</span></p>
    </div>
  </div>

  <div class="block" style="height:248px">
    <div class="deco" style="left:25px;top:70px;width:18px;height:100px"></div>
    <div class="frame" style="left:75px;top:148px;width:93px;height:26px"></div>
    <div class="photo" role="img" aria-label="Portrait photo of analyst Sofia Marrin" style="left:41px;top:28px"></div>
    <div class="bio" style="left:186px;top:26px;width:217px">
      <h3>Sofia Marrin, '22 BS Finance and Marketing,</h3>
      <p>Sofia is a junior at the Gerald P. Ashcombe School of Management majoring in Finance and Marketing. As a complement to her major studies, she is also pursuing an Information Management and Technology minor. Her love for helping others achieve their dreams through financial stability has fueled her charitable work through nonprofit organizations from an early age. Her drive to help others has been carried out through the honors program, a new outlet for her to continue her charitable work through college. On campus, she is an active member of a business fraternity, a house manager, and a volunteer panelist for the academic integrity office. She grew up surrounded by the work her father did as an associate vice president at a bank, which first sparked her interest in financial services. Over a decade later, she is looking forward to pursuing her passion for business and her skills polished through the Trust into her upcoming internship as a summer analyst in securities services. She plans to use the skills she has learned during her time as an analyst as the foundation for her career.</p>
      <p>You can contact Sofia at: <span class="mail">sofia.marrin@birchwoodequity.com</span></p>
    </div>
  </div>

  <div class="block orange" style="height:183px">
    <div class="deco" style="left:345px;top:80px;width:100px;height:103px"></div>
    <div class="frame" style="left:350px;top:115px;width:70px;height:26px"></div>
    <div class="photo" role="img" aria-label="Portrait photo of analyst Ethan Holloway" style="left:283px;top:22px"></div>
    <div class="bio" style="left:41px;top:20px;width:218px">
      <h3>Ethan Holloway, '22 BS Finance and Accounting,</h3>
      <p>Ethan is a junior in the Gerald P. Ashcombe School of Management, double majoring in finance and accounting. His interest in finance stems from his fascination in market trends and how the operations and strategies of different types of businesses help them achieve their goals. Outside of the classroom, he is Vice President of the investment club and a volunteer at a local elementary school where he assists students with their reading and writing skills. This past summer, he was a bank capital analyst intern where he built loan level reports, board reports, and stress testing models catered to recent events. He looks forward to developing his skillset through his classes and the Trust for future endeavors in the world of business.</p>
      <p>You can contact Ethan at: <span class="mail">ethan.holloway@birchwoodequity.com</span></p>
    </div>
  </div>

  <div class="block" style="height:189px">
    <div class="deco" style="left:25px;top:30px;width:18px;height:100px"></div>
    <div class="frame" style="left:17px;top:95px;width:40px;height:26px"></div>
    <div class="photo" role="img" aria-label="Portrait photo of analyst Simon Rask" style="left:41px;top:27px"></div>
    <div class="bio" style="left:186px;top:25px;width:217px">
      <h3>Simon Rask, '22 BS Finance and Accounting,</h3>
      <p>Simon is a junior analyst at the Birchwood Equity Trust, studying finance and accounting in the Gerald P. Ashcombe School of Management. His passion for business was triggered at a young age when he founded a sneaker re-sale website. His ambition and experience in financial markets led to his appointment as President of the investment club and his upcoming summer analyst opportunity in corporate and investment banking. He is a citizen who enjoys traveling and snowboarding in his free time.</p>
      <p>You can contact Simon at: <span class="mail">simon.rask@birchwoodequity.com</span></p>
    </div>
  </div>

  <div class="block orange" style="height:183px">
    <div class="deco" style="left:262px;top:100px;width:110px;height:83px"></div>
    <div class="frame" style="left:263px;top:140px;width:70px;height:28px"></div>
    <div class="photo" role="img" aria-label="Portrait photo of analyst Yuri Danel" style="left:283px;top:22px"></div>
    <div class="bio" style="left:41px;top:20px;width:218px">
      <h3>Yuri Danel, '22 BS Finance, Data Analytics and Economics,</h3>
      <p>Born and raised abroad, Yuri is a junior at the university majoring in finance with minors in data analytics and economics. He is currently interning at a ministry of finance, particularly the debt policy department, where he is gaining experience in the issuance and sale of sovereign bonds. He is developing his leadership skills by being a member of a student cultural club, where he helps to organize events that spread awareness about issues his home country is facing, as well as helps new students get used to college life.</p>
      <p>You can contact Yuri at: <span class="mail">yuri.danel@birchwoodequity.com</span></p>
    </div>
  </div>

  <div class="block" style="height:188px">
    <div class="deco" style="left:25px;top:0;width:110px;height:105px"></div>
    <div class="frame" style="left:17px;top:85px;width:40px;height:26px"></div>
    <div class="photo" role="img" aria-label="Portrait photo of analyst Peter Lindqvist" style="left:41px;top:27px"></div>
    <div class="bio" style="left:186px;top:25px;width:217px">
      <h3>Peter Lindqvist, '22 BS Finance and Accounting,</h3>
      <p>Peter is a junior in the Gerald P. Ashcombe School of Management, majoring in finance and accounting with a minor in economics. His passion for finance comes from his desire to help others and create positive change. He has been managing a portfolio of his own savings since 2018. Along with being a junior analyst in the Trust, he is also a member of a business fraternity, where he is a finance tutor, was on the events committee, and participates in a tax program. He is also on the club tennis team, as well as an avid chess player. He is always looking to learn and believes the Trust will help build a holistic business foundation for his future. This summer he looks forward to interning as a summer financial analyst.</p>
      <p>You can contact Peter at: <span class="mail">peter.lindqvist@birchwoodequity.com</span></p>
    </div>
  </div>

  <div class="block orange" style="height:202px">
    <div class="deco" style="left:262px;top:90px;width:120px;height:80px"></div>
    <div class="frame" style="left:323px;top:140px;width:97px;height:28px"></div>
    <div class="deco" style="left:0;top:150px;width:18px;height:52px"></div>
    <div class="photo" role="img" aria-label="Portrait photo of analyst Mei Lorren" style="left:283px;top:22px"></div>
    <div class="bio" style="left:41px;top:20px;width:218px">
      <h3>Mei Lorren, '22 BS Finance and Information Management &amp; Technology</h3>
      <p>Mei is a junior dual major in Finance at the Gerald P. Ashcombe School of Management and Information Management and Technology at the school of information studies with a minor in a second language. She enjoys getting actively involved in her community. On campus, she is a tour guide for the university, a middle school volunteer tutor, and treasurer for a student association. Having been selected to go on the Wall Street trip, she got to picture herself working in the financial industry. Through these opportunities, she's been able to grow and network with mentors in various fields which ultimately led her to the Trust. She hopes to keep widening her skillset and pursue a career in financial services. She has accepted a summer analyst position in security services.</p>
      <p>You can contact Mei at: <span class="mail">mei.lorren@birchwoodequity.com</span></p>
    </div>
  </div>

  <footer class="footer">
    <div class="f-brand">The Birchwood Equity Trust, LLC</div>
    <div class="f-col" style="left:185px"><b><svg width="5" height="6" viewBox="0 0 10 12"><path d="M5 0a4 4 0 0 1 4 4c0 3-4 8-4 8S1 7 1 4a4 4 0 0 1 4-4z" fill="#fff"/></svg>VISIT US</b>Managing Director<br>The GPA Ashcombe Professor of Finance</div>
    <div class="f-col" style="left:302px"><b><svg width="6" height="6" viewBox="0 0 12 12"><path d="M2 1l2 0 1 3-1.5 1a7 7 0 0 0 3.5 3.5L8 7l3 1v2a1 1 0 0 1-1 1A9 9 0 0 1 1 2a1 1 0 0 1 1-1z" fill="#fff"/></svg>CONTACT US</b>555.014.2290<br>r.ostrano@birchwoodequity.com</div>
    <div class="legal">The Birchwood Equity Trust, LLC is a private investments fund organized as a Delaware Limited Liability Company. The Fund is an entity operated by a board of directors. Managing Directors, and recruited students of the Gerald P. Ashcombe School of Management.<br>This website serves information and educational purposes only.<br>The website does not constitute an offer to sell or a solicitation of an offer to buy securities. Such offers may be made only pursuant to a private placement memorandum, and securities will be sold only to investors who meet certain suitability requirements.<br>2023 The Birchwood Equity Trust, LLC. All Rights Reserved.</div>
  </footer>
</section>

</div>
</body>
</html>
```